Legal and business training card design

We need a business card design for POBAK - Pastoral Owners Bureau and Knowhow Agency a new company set up in county Victoria . Our aim is to assist regional business with their every day employment law legal issues and questions - this would include compliance within the workplace, employment conts, EBAs, dismissals, and general OHS. As well as POBAK will engage in training in particular Human Resources, management v leadership, time management , as well as constructing training around individual business/s needs. So we are multi purpose.
Our product is our service. It's designed specifically for regional base business hence we understand the requirements and needs of regional business v city business. At the same time the card must be simple, yet hard hitting, getting the message across in a couple of seconds.
I would like to see red and yellows, with perhaps a symbol/logo that represents the regional areas incorporated into the POBAK name ie curvy R in which the R's " right leg "expands under the entire acronym. Or you may have some better ideas. I also like the symbol of the square/s to match our slogan "designing employment solutions outside the square".
Thanks
Industry/Entity Type
Training
Contact Information for Business Card
POBAK
Pastoral Owners Bureau & Knowhow Agency
"Designing employment solutions outside the square"
Fiona Brack B.A LL.B
Director and Principal
T: 1800 927 418 E: fiona@pobak.com.au
W: www.pobak.com.au

```html
<!DOCTYPE html>
<html lang="en">
<head>
<meta charset="utf-8">
<title>POBAK business card</title>
<link href="https://fonts.googleapis.com/css2?family=Roboto+Condensed:wght@400;700&display=swap" rel="stylesheet">
<style>
  :root {
    --page: #e9e7e4;
    --ink: #0b0b0b;
    --red: #e0062e;
    --red-deep: #a80f2a;
    --rule: #e6e6e6;
    --white: #ffffff;
  }
  * { margin: 0; padding: 0; box-sizing: border-box; }
  html, body { width: 1200px; height: 1023px; overflow: hidden; }
  body {
    background: var(--page);
    font-family: "Roboto Condensed", "Arial Narrow", sans-serif;
    position: relative;
  }
  .card {
    position: absolute;
    left: 200px;
    width: 800px;
    height: 457px;
    overflow: hidden;
    box-shadow: 0 10px 30px rgba(0,0,0,.18);
  }
  .card--front { top: 30px; }
  .card--back { top: 536px; }
  .card__art { position: absolute; inset: 0; width: 100%; height: 100%; }

  .company {
    position: absolute;
    color: var(--red);
    font-weight: 700;
    line-height: 1.05;
  }
  .card--front .company {
    left: 44px; top: 46px;
    font-size: 34px;
  }
  .person {
    position: absolute;
    right: 48px; top: 118px;
    text-align: right;
    color: var(--white);
  }
  .person__name {
    color: var(--red);
    font-size: 46px;
    font-weight: 700;
    line-height: 1;
  }
  .person__title { font-size: 17px; margin-top: 6px; }
  .contact {
    position: absolute;
    right: 48px; top: 230px;
    list-style: none;
    color: var(--white);
    font-size: 21px;
    line-height: 1.55;
    text-align: right;
  }
  .contact li { display: flex; justify-content: flex-end; align-items: center; gap: 12px; }
  .contact svg { width: 18px; height: 18px; fill: var(--white); }

  .brand-name {
    position: absolute;
    left: 44px; top: 372px;
    display: flex; align-items: center; gap: 14px;
    color: var(--white);
    font-size: 56px;
    font-weight: 400;
    letter-spacing: 2px;
    line-height: 1;
  }
  .brand-name__square {
    width: 20px; height: 20px;
    background: var(--white);
  }

  .back-text {
    position: absolute;
    left: 0; right: 0; top: 70px;
    text-align: center;
  }
  .back-text__name {
    color: var(--white);
    font-size: 104px;
    font-weight: 400;
    letter-spacing: 4px;
    line-height: 1;
  }
  .card--back .company {
    position: static;
    font-size: 36px;
    margin-top: 14px;
  }
  .tagline {
    color: var(--white);
    font-size: 20px;
    margin-top: 8px;
  }
</style>
</head>
<body>

<section class="card card--front">
  <svg class="card__art" viewBox="0 0 800 457" aria-hidden="true">
    <defs>
      <linearGradient id="front-black" x1="0" y1="0" x2="1" y2="1">
        <stop offset="0" stop-color="#1c1c1c"/>
        <stop offset="0.5" stop-color="#050505"/>
        <stop offset="1" stop-color="#141414"/>
      </linearGradient>
      <linearGradient id="front-red" x1="0" y1="0" x2="1" y2="1">
        <stop offset="0" stop-color="#d5022a"/>
        <stop offset="1" stop-color="#e6345a"/>
      </linearGradient>
    </defs>
    <rect width="800" height="457" fill="url(#front-black)"/>
    <rect x="548" y="22" width="46" height="22" fill="var(--rule)"/>
    <rect x="612" y="0" width="188" height="50" fill="var(--white)"/>
    <path d="M0 236 Q 280 420 600 457" fill="none" stroke="var(--rule)" stroke-width="9"/>
    <path d="M0 244 Q 270 425 585 457 L0 457 Z" fill="var(--red-deep)"/>
    <path d="M0 260 Q 260 432 560 457 L0 457 Z" fill="url(#front-red)"/>
  </svg>

  <h1 class="company">Pastoral Owners Bureau<br>&amp; Knowhow Agency</h1>
  <div class="brand-name"><span class="brand-name__square"></span>POBAK</div>

  <div class="person">
    <p class="person__name">Fiona Brack</p>
    <p class="person__title">B.A LL.B Director and Principal</p>
  </div>

  <ul class="contact">
    <li>1800 927 418
      <svg viewBox="0 0 24 24"><path d="M6.6 10.8a15.1 15.1 0 0 0 6.6 6.6l2.2-2.2a1 1 0 0 1 1-.25 11.4 11.4 0 0 0 3.6.57 1 1 0 0 1 1 1V20a1 1 0 0 1-1 1A17 17 0 0 1 3 4a1 1 0 0 1 1-1h3.5a1 1 0 0 1 1 1c0 1.250.2 2.45.57 3.57a1 1 0 0 1-.25 1z"/></svg>
    </li>
    <li>www.pobak.com.au
      <svg viewBox="0 0 24 24"><path d="M3 4h18v13H3zM5 6v9h14V6zM8 19h8v2H8z"/></svg>
    </li>
    <li>fiona@pobak.com.au
      <svg viewBox="0 0 24 24"><path d="M2 5h20v14H2zm2 2v.4l8 5 8-5V7zm0 2.8V17h16V9.8l-8 5z"/></svg>
    </li>
  </ul>
</section>

<section class="card card--back">
  <svg class="card__art" viewBox="0 0 800 457" aria-hidden="true">
    <defs>
      <linearGradient id="back-black" x1="0" y1="0" x2="1" y2="1">
        <stop offset="0" stop-color="#050505"/>
        <stop offset="0.45" stop-color="#262626"/>
        <stop offset="1" stop-color="#0a0a0a"/>
      </linearGradient>
      <linearGradient id="back-red" x1="0" y1="0" x2="1" y2="1">
        <stop offset="0" stop-color="#d9385c"/>
        <stop offset="1" stop-color="#d5022a"/>
      </linearGradient>
    </defs>
    <rect width="800" height="457" fill="url(#back-black)"/>
    <path d="M0 380 Q 470 400 800 250" fill="none" stroke="var(--rule)" stroke-width="9"/>
    <path d="M0 388 Q 470 408 800 258 L800 457 L0 457 Z" fill="var(--red-deep)"/>
    <path d="M0 402 Q 470 420 800 274 L800 457 L0 457 Z" fill="url(#back-red)"/>
  </svg>

  <div class="back-text">
    <p class="back-text__name">POBAK</p>
    <h2 class="company">Pastoral Owners Bureau &amp; Knowhow Agency</h2>
    <p class="tagline">“Designing employment solutions outside the square”</p>
  </div>
</section>

</body>
</html>
```